Over The Ridge Mediaworks Business Card
Card design
Over The Ridge Mediaworks Business Card -
Creative Brief
Simple
Simon Ashby
Chief Creative Officer
no address
Simon.Ashby@OverTheRidgeMediaworks.example
OverTheRidgeMediaworks.example
I don't have the source files from my logo project yet but will be uploading soon. Meanwhile please go to: http://entries.markcraftstudio.example/contests/over-the-ridge-logo and refer to winning draft #73 (also draft #5) I would like the front of the card to have the red-background logo plus the web address only
The back of the card will have the black-background logo plus all the personal information in white lettering. I would also like to see a version with the white-background logo and black lettering

```html
<!DOCTYPE html>
<html lang="en">
<head>
<meta charset="utf-8">
<title>Over The Ridge Mediaworks Business Card</title>
<link href="https://fonts.googleapis.com/css2?family=Montserrat:wght@400;500;800&display=swap" rel="stylesheet">
<style>
  :root {
    --board: #2b2b2b;
    --card-white: #ffffff;
    --card-black: #1c1c1c;
    --brand-red: #c8201f;
    --band-red-text: #7a1212;
    --ink: #1a1a1a;
    --muted: #6e6e6e;
    --label: #e6e6e6;
  }
  * { box-sizing: border-box; margin: 0; padding: 0; }
  html, body { width: 1200px; height: 806px; overflow: hidden; }
  body {
    background: var(--board);
    font-family: "Montserrat", sans-serif;
    position: relative;
  }
  .card {
    position: absolute;
    width: 478px;
    height: 269px;
    border-radius: 22px;
    overflow: hidden;
  }
  .front-a { left: 91px; top: 43px; background: var(--card-white); }
  .front-b { left: 643px; top: 43px; background: var(--brand-red); }
  .back-a  { left: 91px; top: 422px; background: var(--card-white); }
  .back-b  { left: 643px; top: 422px; background: var(--card-black); }

  .web-band {
    position: absolute;
    left: 0; right: 0;
    display: flex; align-items: center; justify-content: center;
    font-variant: small-caps;
    letter-spacing: 1.5px;
    font-size: 12px;
  }
  .front-a .web-band { top: 29px; height: 19px; background: var(--brand-red); color: var(--band-red-text); }
  .front-b .web-band { top: 0; height: 53px; padding-top: 12px; background: var(--card-black); color: #f2f2f2; }

  .wordmark {
    position: absolute;
    left: 0; right: 0; top: 100px;
    display: flex; align-items: center; justify-content: center; gap: 12px;
  }
  .front-b .wordmark { top: 108px; }
  .wordmark-text {
    font-weight: 800;
    text-transform: uppercase;
    line-height: 1.05;
    text-align: left;
  }
  .wordmark-text .line-main { display: block; font-size: 34px; letter-spacing: 1px; }
  .wordmark-text .line-sub  { display: block; font-size: 14px; letter-spacing: 4px; }
  .front-a .wordmark-text { color: var(--ink); }
  .front-b .wordmark-text { color: var(--card-white); }
  .wordmark-dot { width: 22px; height: 22px; border-radius: 50%; }
  .front-a .wordmark-dot { background: var(--brand-red); }
  .front-b .wordmark-dot { background: var(--card-black); }

  .person-name {
    position: absolute; left: 0; right: 0; top: 118px;
    text-align: center;
    color: var(--brand-red);
    font-variant: small-caps;
    font-size: 22px;
    letter-spacing: 2px;
  }
  .person-title {
    position: absolute; left: 0; right: 0; top: 148px;
    text-align: center;
    font-variant: small-caps;
    font-size: 12px;
    letter-spacing: 1px;
  }
  .back-a .person-title { color: var(--ink); }
  .back-b .person-title { color: #d8d8d8; }

  .contact-line {
    position: absolute; left: 24px; top: 221px;
    font-variant: small-caps;
    font-size: 10px;
    letter-spacing: 1px;
    white-space: nowrap;
  }
  .back-a .contact-line { color: var(--muted); }
  .back-b .contact-line { color: #a8a8a8; }
  .contact-line .divider { margin: 0 6px; }
  .contact-rule {
    position: absolute; left: 20px; top: 237px;
    width: 420px; height: 1px;
  }
  .back-a .contact-rule { background: linear-gradient(90deg, #bdbdbd, rgba(189,189,189,0)); }
  .back-b .contact-rule { background: linear-gradient(90deg, #555, rgba(85,85,85,0)); }

  .card-label {
    position: absolute;
    width: 478px;
    text-align: center;
    color: var(--label);
    font-variant: small-caps;
    font-size: 20px;
    letter-spacing: 2px;
  }
  .label-front-a { left: 91px;  top: 352px; }
  .label-front-b { left: 643px; top: 352px; }
  .label-back-a  { left: 91px;  top: 750px; }
  .label-back-b  { left: 643px; top: 750px; }
</style>
</head>
<body>
  <section class="card front-a">
    <div class="web-band">OverTheRidgeMediaworks.example</div>
    <div class="wordmark">
      <div class="wordmark-text"><span class="line-main">Over The Ridge</span><span class="line-sub">Mediaworks</span></div>
      <span class="wordmark-dot"></span>
    </div>
  </section>
  <div class="card-label label-front-a">Business Card Front A</div>

  <section class="card front-b">
    <div class="web-band">OverTheRidgeMediaworks.example</div>
    <div class="wordmark">
      <div class="wordmark-text"><span class="line-main">Over The Ridge</span><span class="line-sub">Mediaworks</span></div>
      <span class="wordmark-dot"></span>
    </div>
  </section>
  <div class="card-label label-front-b">Business Card Front B</div>

  <section class="card back-a">
    <div class="person-name">Simon Ashby</div>
    <div class="person-title">Chief Creative Officer</div>
    <div class="contact-line">310 555 0142<span class="divider">|</span>Simon.Ashby@OverTheRidgeMediaworks.example</div>
    <div class="contact-rule"></div>
  </section>
  <div class="card-label label-back-a">Business Card Back A</div>

  <section class="card back-b">
    <div class="person-name">Simon Ashby</div>
    <div class="person-title">Chief Creative Officer</div>
    <div class="contact-line">310 555 0142<span class="divider">|</span>Simon.Ashby@OverTheRidgeMediaworks.example</div>
    <div class="contact-rule"></div>
  </section>
  <div class="card-label label-back-b">Business Card Back B</div>
</body>
</html>
```